Monthly Mailed Newsletter/Magazine for Medical Spa

Every month we send out a mailed newsletter/magazine to our visitors from the previous month. We made a sample newsletter/magazine as a guideline of what we are looking for. We need a designer to make a simple and clean design layout.

- Attached is our sample design that has all the content we want to use.
- Newsletter/magazine is 8 pages total.
- Size of each page is 8.5 inches in width by 11 inches in height.
- Content and images can be located here: https://files.vornacloud.net/shared/8kqTRw3ZpLmX2vNcA7yHd5EbJ0sUgFo4e?view=open

The following will give you an idea of our brand presentation.
Our website is: www.GlowDermaClinic.com
Our Instagram; @glowdermaclinic
Our Facebook: www.socialtreo.com/glowdermaclinic

Target Market(s)

Women 25 - 45

Industry/Entity Type

Beauty

Font styles to use
Other font styles liked:
• Josefins Sans Bold & Lato

Colors
f78f20
ffffff

Requirements
Must have
• - Our Logo
- Our tagline: YOUR SKIN DESERVES IT!
- Address and contact information for our locations
- Our color scheme: Black and #FAA641
- Heading font is Josefin Sans Bold
- Paragraph font is Lato
- Our website address: www.GlowDermaClinic.com

```html
<!DOCTYPE html>
<html lang="en">
<head>
<meta charset="utf-8">
<title>Contents</title>
<link rel="stylesheet" href="https://fonts.googleapis.com/css2?family=Josefin+Sans:ital,wght@0,300;0,700;1,300&display=swap">
<style>
  :root {
    --orange: #f78f20;
    --orange-soft: #f9a64f;
    --peach: #fcd9b4;
    --peach-pale: #fde3c6;
    --white: #ffffff;
    --ink: #1a1a1a;
  }
  html, body { margin: 0; padding: 0; overflow: hidden; }
  .page {
    position: relative;
    width: 927px;
    height: 1200px;
    overflow: hidden;
    font-family: "Josefin Sans", sans-serif;
    background: linear-gradient(180deg, var(--peach-pale) 197px, var(--peach) 330px, var(--orange-soft) 620px, var(--orange-soft) 1200px);
  }
  .masthead {
    position: absolute; left: 0; top: 0; width: 927px; height: 200px;
    background: linear-gradient(180deg, var(--orange-soft) 0%, #fbc88e 45%, var(--white) 100%);
  }
  .masthead-title {
    position: absolute; left: 30px; top: 72px; margin: 0;
    font-weight: 700; font-size: 58px; letter-spacing: 2px; color: var(--white);
  }
  .photo { position: absolute; }
  .photo-round { border-radius: 50%; }
  .photo-treatment {
    left: 7px; top: 219px; width: 364px; height: 364px;
    background: linear-gradient(160deg, #c9b46a 0%, #e8b24c 40%, #f2a987 70%, #e9c07a 100%);
  }
  .photo-mirror {
    left: 53px; top: 583px; width: 318px; height: 318px;
    background: linear-gradient(120deg, #e9d6c6 0%, #d9c2b0 45%, #3a2a26 75%, #c9a48e 100%);
  }
  .photo-staff {
    left: 0; top: 848px; width: 197px; height: 352px;
    background: linear-gradient(180deg, #e6e2dc 0%, #c9bfc6 40%, #3b3236 75%, #2a2427 100%);
  }
  .entry-number {
    position: absolute; margin: 0;
    font-weight: 700; font-size: 46px; line-height: 46px; color: var(--white);
  }
  .entry-number--accent { color: var(--orange); }
  .entry-heading {
    position: absolute; margin: 0; text-align: right;
    font-weight: 700; font-size: 27px; line-height: 35px; letter-spacing: 1px;
    color: var(--white); text-transform: uppercase;
  }
  .entry-heading--pale { color: var(--peach-pale); }
  .entry-summary {
    position: absolute; margin: 0; text-align: right;
    font-weight: 300; font-style: italic; font-size: 27px; line-height: 35px; color: var(--ink);
  }
  .entry-summary b { font-style: normal; }
</style>
</head>
<body>
<main class="page">
  <header class="masthead">
    <h1 class="masthead-title">CONTENTS</h1>
  </header>

  <div class="photo photo-round photo-treatment" role="img" aria-label="Gloved hand holding a laser hair removal device against skin"></div>
  <div class="photo photo-round photo-mirror" role="img" aria-label="Client looking into a hand mirror after treatment"></div>
  <div class="photo photo-staff" role="img" aria-label="Clinic staff member in a face mask holding a skincare product"></div>

  <p class="entry-number entry-number--accent" style="left:427px; top:341px;">03</p>
  <h2 class="entry-heading entry-heading--pale" style="right:89px; top:277px;">November 2020<br>Promotions</h2>
  <p class="entry-summary" style="right:89px; top:352px;">Don't miss out on<br>end of the year<br>promotions.</p>

  <p class="entry-number" style="left:400px; top:613px;">04</p>
  <h2 class="entry-heading" style="right:82px; top:545px;">Is at-home laser hair<br>removal effective?</h2>
  <p class="entry-summary" style="right:82px; top:617px;">Here are some unbiased<br>professional opinions<br>to zap away your FAQs<b>.</b></p>

  <p class="entry-number" style="left:291px; top:841px;">06</p>
  <h2 class="entry-heading" style="right:82px; top:806px;">Can you make your Velatox<br>last longer?</h2>
  <p class="entry-summary" style="right:82px; top:876px;">We sought advice from professionals<br>to bring you the answer.</p>

  <p class="entry-number" style="left:227px; top:1033px;">08</p>
  <h2 class="entry-heading" style="right:89px; top:1023px;">Preview of next weeks issue</h2>
  <p class="entry-summary" style="right:89px; top:1056px;">Take a peak at what's coming next!</p>
</main>
</body>
</html>
```